Bayline Pet Rehoming GALA

Hi ALL!
We need an 8.5 X 11 inch, one page flyer to include all the below copy plus 8 sponsoring logos at the very bottom.
Thank YOU!

Corvel Heights Pet GALA
(Fun for Animals In Rescue!)

Sunday, August 12, 2018
1 to 4:30 p.m.

Animal Education & Adoption Event
featuring:

BK Pet Shelter & Services Rabbits & Mice

Hilltop Browsing Sheep

Thankful Hounds Haven

Featherwell Finches & Larks

Comet Pup Haven

Marla’s Feline Haven

Marvel Pup Haven

Special Guest from 1-3 p.m.
BeeBop - SF's 1st Therapy Pig!
Instagram: @BEEBOP_BKHOG
Facebook: @BEEBOP THE HOG

Activities for Kids
Dog & Cat Toy Making with Greta Vossel Canine Coaching
Animal Mask Making with Tiny Crafters
Face-in-a-Hole Photo Fun with Hugo Marsh Canine Coaching

BK PSS FREE Giveaway!
First 75 attending families receive a FREE PSS Doggie Bag containing a dog water bottle, food, shampoo, toy, treats and blinking dog collar light.

Animal Tails

1 pm Wendell’s Nook Storytime

1:30 p.m. BeeBop the Therapy Pig

1:45 pm “Tuft the Saved Hog”
Read by Author Marnie Oakhurst

2 p.m. Wendell’s Nook Singalong

2:30 p.m. Featherwell Finch Haven

2:45 p.m. Quire Pages Storytime

3 pm Browsing Sheep Refuge

3:15 p.m. The Burrow Den Puppet Show

3:45 pm BK PSS Officer Tamsin

4 p.m. Wendell’s Nook Storytime

Font styles to use
Serif

Colors

Designer to choose colors to be used in the design.

Requirements
Must have
• pig, goat, 2 dogs, kitten, dove, bunny

```html
<!DOCTYPE html>
<html lang="en">
<head>
<meta charset="utf-8">
<title>Corvel Heights Pet GALA</title>
<link href="https://fonts.googleapis.com/css2?family=Source+Sans+3:wght@400;600;700&family=Titan+One&display=swap" rel="stylesheet">
<style>
:root{
  --green:#8cc63f;
  --green-dark:#6fae2a;
  --blue:#1b3f94;
  --blue-deep:#0f2566;
  --blue-light:#2a63b8;
  --orange:#f7941d;
  --orange-light:#fbad3c;
  --paper:#f2f2f2;
  --grey-text:#7a7a7a;
  --heading-blue:#2e3192;
  --white:#ffffff;
}
*{margin:0;padding:0;box-sizing:border-box}
html,body{width:1000px;height:1200px;overflow:hidden;background:var(--paper)}
body{font-family:"Source Sans 3",Arial,sans-serif;position:relative}
.flyer{position:absolute;inset:0;width:1000px;height:1200px;overflow:hidden}
.backdrop{position:absolute;inset:0}
.animal-group{position:absolute;left:270px;top:18px;width:720px;height:430px;border-radius:46% 46% 30% 30%;
  background:radial-gradient(ellipse at 50% 55%,rgba(240,226,200,.95) 0%,rgba(226,196,160,.8) 45%,rgba(200,214,170,0) 75%)}
.title{position:absolute;left:36px;top:14px;color:var(--white)}
.title-top{font-size:39px;font-weight:400;letter-spacing:.3px;line-height:1;white-space:nowrap}
.title-main{font-family:"Titan One",Impact,sans-serif;font-size:86px;line-height:1;letter-spacing:10px;margin-top:10px}
.tagline{position:absolute;left:27px;top:222px;color:var(--white);font-weight:700;font-size:42px;line-height:43px}
.event-date{position:absolute;left:27px;top:360px;color:var(--white);font-weight:600;font-size:20px;line-height:26px}
.featuring{position:absolute;left:27px;top:536px;color:var(--heading-blue);font-size:29px;line-height:35px;font-weight:400}
.partner-list{position:absolute;left:27px;top:622px;list-style:none}
.partner-list li{display:flex;align-items:center;height:34px;font-size:22px;color:var(--grey-text);white-space:nowrap}
.bullet{width:16px;height:16px;margin-right:14px;flex:none}
.info-panel{position:absolute;left:505px;top:482px;width:470px}
.panel-tab{display:inline-block;background:var(--green);color:var(--white);font-size:24px;line-height:42px;padding:0 22px 0 20px;border-radius:0 12px 12px 0;box-shadow:2px 3px 4px rgba(0,0,0,.2)}
.panel-copy{color:var(--white);font-size:16px;line-height:18.5px;padding:10px 0 12px 20px}
.tails{list-style:none;padding:10px 0 0 20px;color:var(--white);font-size:13.4px;line-height:18.3px}
.tails b{font-weight:700}
.guest-photo{position:absolute;left:104px;top:914px;width:276px;height:276px;border-radius:50%;background:var(--orange);border:4px solid var(--white);box-shadow:0 2px 6px rgba(0,0,0,.25)}
.guest-photo-inner{position:absolute;inset:14px;border-radius:50%;border:4px solid var(--white);
  background:linear-gradient(180deg,#3d8ee0 0%,#7cb6ea 50%,#c9b7ad 72%,#8a7a6a 100%)}
.guest-pill{position:absolute;left:565px;top:1033px;width:320px;height:40px;border-radius:12px;background:var(--orange);color:var(--white);font-size:23px;line-height:40px;text-align:center;white-space:nowrap;box-shadow:2px 3px 5px rgba(0,0,0,.3)}
.guest-name{position:absolute;left:505px;top:1088px;width:450px;text-align:center;color:var(--white);font-size:31px;line-height:40px;white-space:nowrap}
.socials{position:absolute;left:505px;top:1142px;width:450px;display:flex;justify-content:center;gap:26px;color:var(--white);font-size:18px;line-height:24px;white-space:nowrap}
.social{display:flex;align-items:center;gap:9px}
.social-dot{width:18px;height:18px;border-radius:50%;background:var(--green);flex:none}
</style>
</head>
<body>
<main class="flyer">
  <svg class="backdrop" viewBox="0 0 1000 1200" width="1000" height="1200" aria-hidden="true">
    <defs>
      <linearGradient id="greenFill" x1="0" y1="0" x2="1" y2="1">
        <stop offset="0" stop-color="#9fd04f"/><stop offset="1" stop-color="#7dbb34"/>
      </linearGradient>
      <linearGradient id="blueFill" x1="0" y1="0" x2="1" y2="0">
        <stop offset="0" stop-color="#2a63b8"/><stop offset="1" stop-color="#0f2566"/>
      </linearGradient>
      <linearGradient id="orangeFill" x1="0" y1="0" x2="0" y2="1">
        <stop offset="0" stop-color="#fbad3c"/><stop offset="1" stop-color="#f7941d"/>
      </linearGradient>
    </defs>
    <rect width="1000" height="1200" fill="var(--paper)"/>
    <rect x="512" y="420" width="463" height="620" fill="url(#orangeFill)"/>
    <path d="M0 438 C70 470 160 510 320 518 C600 528 800 430 1000 410 V432 C800 452 600 548 320 540 C160 536 60 505 0 480 Z" fill="url(#blueFill)"/>
    <path d="M0 425 C70 460 160 500 320 506 C600 514 800 420 1000 400 V418 C800 438 600 530 320 522 C160 518 60 482 0 456 Z" fill="var(--white)"/>
    <path d="M0 0 H1000 V400 C800 418 600 508 320 500 C160 496 70 460 0 428 Z" fill="url(#greenFill)"/>
    <path d="M0 0 H495 L566 124 C430 112 300 130 190 168 C110 196 50 205 0 212 Z" fill="url(#blueFill)"/>
    <path d="M0 975 C150 1015 300 1040 500 1015 C700 990 850 968 1000 958 V1200 H0 Z" fill="var(--green)"/>
    <path d="M0 985 C150 1025 300 1050 500 1026 C700 1002 850 980 1000 970 V1200 H0 Z" fill="var(--white)"/>
    <path d="M0 995 C150 1035 300 1060 500 1038 C700 1014 850 993 1000 983 V1200 H0 Z" fill="url(#blueFill)"/>
  </svg>

  <div class="animal-group" role="img" aria-label="Photo group of a bulldog, a golden retriever, a rabbit, a goat, an orange kitten, a piglet holding yellow flowers and a white dove in flight"></div>

  <header class="title">
    <div class="title-top">Corvel Heights Pet</div>
    <div class="title-main">GALA</div>
  </header>

  <h2 class="tagline">FUN FOR<br>ANIMALS IN<br>RESCUE!</h2>
  <p class="event-date">Sunday, August 12, 2018<br>1 to 4:30 p.m.</p>

  <h3 class="featuring">Animal Education &amp; Adoption<br>Event featuring:</h3>
  <ul class="partner-list">
    <li><svg class="bullet" viewBox="0 0 16 16"><circle cx="8" cy="8" r="8" fill="var(--orange)"/><path d="M6.5 4.5 L10 8 L6.5 11.5" stroke="#fff" stroke-width="2" fill="none"/></svg>BK Pet Shelter &amp; Services Rabbits &amp; Mice</li>
    <li><svg class="bullet" viewBox="0 0 16 16"><circle cx="8" cy="8" r="8" fill="var(--orange)"/><path d="M6.5 4.5 L10 8 L6.5 11.5" stroke="#fff" stroke-width="2" fill="none"/></svg>Hilltop Browsing Sheep</li>
    <li><svg class="bullet" viewBox="0 0 16 16"><circle cx="8" cy="8" r="8" fill="var(--orange)"/><path d="M6.5 4.5 L10 8 L6.5 11.5" stroke="#fff" stroke-width="2" fill="none"/></svg>Thankful Hounds Haven</li>
    <li><svg class="bullet" viewBox="0 0 16 16"><circle cx="8" cy="8" r="8" fill="var(--orange)"/><path d="M6.5 4.5 L10 8 L6.5 11.5" stroke="#fff" stroke-width="2" fill="none"/></svg>Featherwell Finches &amp; Larks</li>
    <li><svg class="bullet" viewBox="0 0 16 16"><circle cx="8" cy="8" r="8" fill="var(--orange)"/><path d="M6.5 4.5 L10 8 L6.5 11.5" stroke="#fff" stroke-width="2" fill="none"/></svg>Comet Pup Haven</li>
    <li><svg class="bullet" viewBox="0 0 16 16"><circle cx="8" cy="8" r="8" fill="var(--orange)"/><path d="M6.5 4.5 L10 8 L6.5 11.5" stroke="#fff" stroke-width="2" fill="none"/></svg>Marla’s Feline Haven</li>
    <li><svg class="bullet" viewBox="0 0 16 16"><circle cx="8" cy="8" r="8" fill="var(--orange)"/><path d="M6.5 4.5 L10 8 L6.5 11.5" stroke="#fff" stroke-width="2" fill="none"/></svg>Marvel Pup Haven</li>
  </ul>

  <section class="info-panel">
    <div class="panel-tab">ACTIVITIES FOR KIDS</div>
    <p class="panel-copy">Dog &amp; Cat Toy Making with Greta Vossel Canine Coaching<br>Animal Mask Making with Tiny Crafters<br>Face-in-a-Hole Photo Fun with Hugo Marsh Canine Coaching</p>
    <div class="panel-tab">BK PSS FREE Giveaway!</div>
    <p class="panel-copy">First 75 attending families receive a FREE PSS<br>Doggie Bag containing a dog water bottle, food,<br>shampoo, toy, treats and blinking dog collar light.</p>
    <div class="panel-tab">ANIMAL TAILS</div>
    <ul class="tails">
      <li><b>1:00 pm</b> - Wendell’s Nook Storytime</li>
      <li><b>1:30 pm</b> - BeeBop the Therapy Pig</li>
      <li><b>1:45 pm</b> - “Tuft the Saved Hog” Read by Author Marnie Oakhurst</li>
      <li><b>2:00 pm</b> - Wendell’s Nook Singalong</li>
      <li><b>2:30 pm</b> - Featherwell Finch Haven</li>
      <li><b>2:45 pm</b> - Quire Pages Storytime</li>
      <li><b>3:00 pm</b> - Browsing Sheep Refuge</li>
      <li><b>3:15 pm</b> - The Burrow Den Puppet Show</li>
      <li><b>3:45 pm</b> - BK PSS Officer Tamsin</li>
      <li><b>4:00 pm</b> - Wendell’s Nook Storytime</li>
    </ul>
  </section>

  <div class="guest-photo">
    <div class="guest-photo-inner" role="img" aria-label="Photo of BeeBop the spotted therapy pig wearing a yellow bow and red harness under a blue sky"></div>
  </div>

  <div class="guest-pill">Special Guest from 1-3 p.m.</div>
  <div class="guest-name">BeeBop - SF's 1st Therapy Pig!</div>
  <div class="socials">
    <span class="social"><span class="social-dot"></span>@BEEBOP_BKHOG</span>
    <span class="social"><span class="social-dot"></span>@BEEBOP THE HOG</span>
  </div>
</main>
</body>
</html>
```